Business card for massage therapy company called Brook Fern Wellness

Need business card for massage therapy company called Brook Fern Wellness. Would like my logo on the front and the back of the card I have 3 options of logos and you can play with what looks better.

Would like this information displayed on the back of the card:

Marcus Ellery
Licensed Massage Therapist
321-555-0147
brookfern-example.com
brookfern_rest_

```html
<!DOCTYPE html>
<html lang="en">
<head>
<meta charset="utf-8">
<title>Brook Fern Wellness – Business Card</title>
<link href="https://fonts.googleapis.com/css2?family=Marcellus&family=Montserrat:wght@500&family=Arimo:wght@400&display=swap" rel="stylesheet">
<style>
  :root {
    --backdrop: #5a5a5a;
    --sage: #6b7259;
    --sage-ink: #6b7259;
    --paper: #ffffff;
    --clay: #c39c7e;
  }
  * { margin: 0; padding: 0; box-sizing: border-box; }
  html, body {
    width: 1200px; height: 1200px; overflow: hidden;
    background: var(--backdrop);
  }
  .canvas { position: relative; width: 1200px; height: 1200px; }

  .card {
    position: absolute;
    left: 262px;
    width: 690px;
    height: 394px;
    overflow: hidden;
  }
  .card--front { top: 158px; background: var(--sage); }
  .card--back { top: 651px; background: var(--paper); }

  /* front */
  .front-brand {
    position: absolute; left: 36px; top: 52px;
    font-family: "Marcellus", serif;
    color: var(--paper);
    font-size: 38px; line-height: 44px;
  }
  .front-brand .brand-sub {
    display: block;
    font-size: 18px; letter-spacing: 6px; line-height: 30px;
    padding-left: 56px;
  }
  .person-name {
    position: absolute; left: 36px; top: 178px;
    font-family: "Montserrat", sans-serif; font-weight: 500;
    font-size: 25px; letter-spacing: 0.5px;
    color: var(--clay);
  }
  .person-role, .address, .contact-list {
    font-family: "Arimo", sans-serif; color: var(--paper);
  }
  .person-role {
    position: absolute; left: 36px; top: 210px; font-size: 15px;
  }
  .address {
    position: absolute; left: 37px; top: 241px;
    font-size: 16px; line-height: 21px; font-style: normal;
  }
  .contact-list {
    position: absolute; left: 36px; top: 295px;
    list-style: none; font-size: 16px; line-height: 21px;
  }
  .contact-list li { display: flex; align-items: center; height: 21px; }
  .contact-list svg { width: 14px; height: 14px; margin-right: 13px; flex: none; }

  .front-circle {
    position: absolute; left: 306px; top: 42px;
    width: 310px; height: 310px;
  }

  /* back */
  .back-circle {
    position: absolute; left: 281px; top: 83px;
    width: 136px; height: 136px;
  }
  .back-brand {
    position: absolute; left: 0; right: 0; top: 222px;
    text-align: center;
    font-family: "Marcellus", serif;
    color: var(--sage-ink);
  }
  .back-brand .brand-main {
    display: block; font-size: 46px; letter-spacing: 3px; line-height: 56px;
    padding-left: 10px;
  }
  .back-brand .brand-sub {
    display: block; font-size: 22px; letter-spacing: 9px; line-height: 30px;
  }
</style>
</head>
<body>
<main class="canvas">

  <section class="card card--front" aria-label="Card front">
    <div class="front-brand">Brook Fern<span class="brand-sub">Wellness</span></div>

    <h1 class="person-name">MARCUS ELLERY</h1>
    <p class="person-role">Licensed Massage Therapist</p>
    <address class="address">412 Alder Row<br>Halden, Canada 10293</address>

    <ul class="contact-list">
      <li>
        <svg viewBox="0 0 24 24" aria-hidden="true"><path fill="#c39c7e" d="M6.6 10.8a15 15 0 0 0 6.6 6.6l2.2-2.2a1 1 0 0 1 1-.25 11.4 11.4 0 0 0 3.6.57 1 1 0 0 1 1 1V20a1 1 0 0 1-1 1A17 17 0 0 1 3 4a1 1 0 0 1 1-1h3.5a1 1 0 0 1 1 1c0 1.25.2 2.45.57 3.57a1 1 0 0 1-.25 1z"/></svg>
        321-555-0147
      </li>
      <li>
        <svg viewBox="0 0 24 24" aria-hidden="true"><rect x="2" y="5" width="20" height="14" fill="#c39c7e"/><path d="M2 5l10 8 10-8" fill="none" stroke="#6b7259" stroke-width="1.6"/></svg>
        info@brookfern-example.com
      </li>
      <li>
        <svg viewBox="0 0 24 24" aria-hidden="true"><circle cx="12" cy="12" r="10" fill="#c39c7e"/><path d="M7 7c2 1 3 3 2 5s1 4 0 6M14 4c0 2 2 3 3 4s-1 3 1 5" fill="none" stroke="#6b7259" stroke-width="1.4"/></svg>
        www.brookfern-example.com
      </li>
    </ul>

    <svg class="front-circle" viewBox="0 0 310 310" aria-hidden="true">
      <circle cx="155" cy="155" r="152" fill="none" stroke="#ffffff" stroke-width="2.4"/>
    </svg>
  </section>

  <section class="card card--back" aria-label="Card back">
    <svg class="back-circle" viewBox="0 0 136 136" aria-hidden="true">
      <circle cx="68" cy="68" r="66" fill="none" stroke="#6b7259" stroke-width="1.3"/>
    </svg>
    <div class="back-brand">
      <span class="brand-main">BROOK FERN</span>
      <span class="brand-sub">WELLNESS</span>
    </div>
  </section>

</main>
</body>
</html>
```